Cosmetic injections clinic needs a fresh looking business card

We need a business card using the supplied logo and color scheme to attract future clients to our clinic. It should be modern and fresh, eye catching and not too busy. Simple and to the point is best. I would like two sided designs with the front indicating address and contact information, and the back in full color with white logo and descriptive information also provided.
Target Market(s)
Clients looking for non surgical beauty enhancements.
Contact Information for Business Card
Lumivela
14, 415 Carrow Ridge Road
Harwick Falls, Northvale
K2P 7W3
Phone: 431-662-0974
Email: info@lumivela-example.com
Requirements
Must have
- -Logo supplied with the name and address of the clinic
- -Back of card in full color with white logo with A small line of text indicating both of the following: Skin renewal advisors and cosmetic treatments
- Located inside the Wayfarer Care Group

```html
<!DOCTYPE html>
<html lang="en">
<head>
<meta charset="utf-8">
<title>Lumivela – Business Card</title>
<link href="https://fonts.googleapis.com/css2?family=Barlow:wght@500;600;700&display=swap" rel="stylesheet">
<style>
  :root {
    --purple: #6a3f9c;
    --pink: #e43f9d;
    --white: #ffffff;
    --backdrop: #e9e6ea;
    --shadow: rgba(40, 20, 50, 0.22);
  }
  * { margin: 0; padding: 0; box-sizing: border-box; }
  html, body { width: 1200px; height: 1000px; overflow: hidden; }
  body {
    background: var(--backdrop);
    font-family: "Barlow", Arial, sans-serif;
    position: relative;
  }
  .card {
    position: absolute;
    width: 560px;
    height: 320px;
    border-radius: 22px;
    overflow: hidden;
    box-shadow: 0 14px 30px var(--shadow);
  }
  /* Front */
  .card-front { left: 50px; top: 100px; background: var(--white); }
  .card-front .wave { position: absolute; inset: 0; width: 100%; height: 100%; }
  .brand {
    display: flex; align-items: center; gap: 12px;
    font-weight: 600; letter-spacing: 1px;
  }
  .brand-mark { border-radius: 50%; flex: none; }
  .card-front .brand {
    position: absolute; left: 340px; top: 92px;
    color: var(--pink); font-size: 34px;
  }
  .card-front .brand-mark { width: 36px; height: 36px; background: var(--purple); }
  .contact {
    position: absolute; left: 40px; top: 150px;
    list-style: none; color: var(--white);
    font-size: 15px; font-weight: 600; line-height: 1.35;
  }
  .contact li { display: flex; gap: 9px; align-items: flex-start; }
  .contact li + li { margin-top: 2px; }
  .contact svg { width: 13px; height: 13px; flex: none; margin-top: 3px; fill: var(--white); }
  /* Back */
  .card-back { left: 590px; top: 580px; background: var(--pink); }
  .card-back .brand {
    position: absolute; left: 0; right: 0; top: 92px; justify-content: center;
    color: var(--white); font-size: 58px; gap: 16px;
  }
  .card-back .brand-mark { width: 52px; height: 52px; background: var(--white); }
  .taglines {
    position: absolute; left: 0; right: 0; top: 210px;
    display: flex; align-items: center; justify-content: center; gap: 18px;
    color: var(--white); font-size: 14px; font-weight: 700;
    text-transform: uppercase; line-height: 1.25;
  }
  .tagline-left { text-align: right; }
  .tagline-right { text-align: left; }
  .tag-dot { width: 11px; height: 11px; border-radius: 50%; background: var(--white); }
</style>
</head>
<body>

<section class="card card-front" aria-label="Business card front">
  <svg class="wave" viewBox="0 0 560 320" preserveAspectRatio="none" aria-hidden="true">
    <path fill="var(--pink)" d="M0 0 H300 C350 0 325 110 380 185 C430 250 490 262 560 258 V320 H0 Z"/>
    <path fill="var(--white)" d="M0 0 H284 C330 0 308 118 364 194 C414 262 482 276 560 272 V320 H0 Z"/>
    <path fill="var(--purple)" d="M0 0 H276 C322 0 300 124 356 200 C406 268 478 284 560 280 V320 H0 Z"/>
  </svg>
  <div class="brand"><span class="brand-mark"></span>Lumivela</div>
  <ul class="contact">
    <li>
      <svg viewBox="0 0 24 24"><path d="M12 2a7 7 0 0 0-7 7c0 5 7 13 7 13s7-8 7-13a7 7 0 0 0-7-7zm0 9.5A2.5 2.5 0 1 1 12 6.5a2.5 2.5 0 0 1 0 5z"/></svg>
      <span>14, 415 Carrow Ridge Road<br>Harwick Falls, Northvale<br>K2P 7W3</span>
    </li>
    <li>
      <svg viewBox="0 0 24 24"><path d="M6.6 10.8a15 15 0 0 0 6.6 6.6l2.2-2.2a1 1 0 0 1 1-.25 11.4 11.4 0 0 0 3.6.57 1 1 0 0 1 1 1V20a1 1 0 0 1-1 1A17 17 0 0 1 3 4a1 1 0 0 1 1-1h3.5a1 1 0 0 1 1 1c0 1.25.2 2.45.57 3.57a1 1 0 0 1-.25 1z"/></svg>
      <span>431-662-0974</span>
    </li>
    <li>
      <svg viewBox="0 0 24 24"><path d="M3 5h18a1 1 0 0 1 1 1v12a1 1 0 0 1-1 1H3a1 1 0 0 1-1-1V6a1 1 0 0 1 1-1zm9 7.5L20 7H4z"/></svg>
      <span>info@lumivela-example.com</span>
    </li>
  </ul>
</section>

<section class="card card-back" aria-label="Business card back">
  <div class="brand"><span class="brand-mark"></span>Lumivela</div>
  <div class="taglines">
    <p class="tagline-left">Skin renewal advisors and<br>cosmetic treatments</p>
    <span class="tag-dot"></span>
    <p class="tagline-right">Located inside the<br>Wayfarer Care Group</p>
  </div>
</section>

</body>
</html>
```